Corvane Quince Bark Extract Supreme Serum - Product Label

Hi Guys,

I threw up a rough label sketch. Looking to keep the label clean and fresh.

LABEL DIMENSIONS: 4.05 in (Height) x 1.18 in (Diameter)

Industry/Entity Type

Beauty Aid

Font styles to use
Serif

Colors
0255a3
0592cd
6b449b
ffc214

Requirements
Must have
• Velloriant
• S K I N
Nice to have
• We can try purple, gold and black or stick with the blue scheme we have going.

```html
<!DOCTYPE html>
<html lang="en">
<head>
<meta charset="utf-8">
<title>Velloriant – Corvane Quince Bark Extract Supreme Serum Label</title>
<link rel="stylesheet" href="https://fonts.googleapis.com/css2?family=Cinzel:wght@500&family=Fira+Sans+Extra+Condensed:wght@400;600&family=Source+Sans+3:wght@300;600&display=swap">
<style>
  :root {
    --page: #ffffff;
    --label-edge: #d7ebf4;
    --label-mid: #f7fbfd;
    --rule: #b9bfc4;
    --brand: #2d5c8f;
    --product: #3a6fb8;
    --serum: #1b44b8;
    --panel-text: #1f4f9e;
    --panel: #ffffff;
    --wave-deep: #1f5fe0;
    --wave-soft: #9fd0f2;
    --badge-one: #f2a9c9;
    --badge-two: #2e9a48;
  }
  * { margin: 0; padding: 0; box-sizing: border-box; }
  html, body {
    width: 1200px; height: 673px; overflow: hidden;
    background: var(--page);
  }
  .canvas { position: relative; width: 1200px; height: 673px; }

  .label {
    position: absolute; left: 25px; top: 82px;
    width: 1150px; height: 508px; overflow: hidden;
    background: radial-gradient(ellipse at 50% 45%, var(--label-mid) 0%, #eef7fb 55%, var(--label-edge) 100%);
  }
  .label__wave { position: absolute; inset: 0; width: 100%; height: 100%; }

  .label__rule {
    position: absolute; top: 51px; left: 0; right: 0;
    height: 2px; background: var(--rule);
  }
  .label__mark {
    position: absolute; top: 40px; left: 563px;
    width: 24px; height: 24px; border-radius: 50%;
    background: var(--wave-deep);
    box-shadow: 0 0 0 6px #ffffff;
  }

  .label__title {
    position: absolute; left: 315px; width: 520px; text-align: center;
  }
  .brand-name {
    top: 112px;
    font-family: "Cinzel", serif; font-weight: 500;
    font-size: 40px; letter-spacing: 2px; color: var(--brand);
  }
  .product-name {
    top: 178px;
    font-family: "Source Sans 3", sans-serif; font-weight: 300;
    font-size: 29px; line-height: 42px; color: var(--product);
    letter-spacing: -0.3px;
  }
  .product-name .product-type {
    display: block; font-weight: 600; color: var(--serum);
  }
  .skin-line {
    top: 312px;
    font-family: "Cinzel", serif; font-weight: 500;
    font-size: 15px; letter-spacing: 6px; color: var(--brand);
  }
  .volume {
    position: absolute; left: 315px; width: 520px; top: 471px;
    text-align: center;
    font-family: "Source Sans 3", sans-serif; font-weight: 300;
    font-size: 16px; color: var(--product);
  }

  .panel {
    position: absolute; top: 77px; width: 223px; height: 404px;
    background: var(--panel);
    font-family: "Fira Sans Extra Condensed", sans-serif;
    font-size: 13px; line-height: 19.5px; color: var(--panel-text);
    letter-spacing: -0.2px; white-space: nowrap;
  }
  .panel--info { left: 62px; padding: 36px 10px 0 43px; }
  .panel--distributor { left: 833px; padding: 16px 10px 0 36px; }
  .panel strong { font-weight: 600; }
  .panel p + p { margin-top: 16px; }

  .badges {
    position: absolute; left: 36px; bottom: 30px;
    display: flex; gap: 14px; align-items: center;
  }
  .badge { width: 50px; height: 50px; border-radius: 50%; }
  .badge--cruelty { background: var(--badge-one); width: 42px; height: 42px; }
  .badge--quality { background: var(--badge-two); }
</style>
</head>
<body>
<main class="canvas">
  <section class="label" aria-label="Serum bottle label">
    <svg class="label__wave" viewBox="0 0 1150 508" role="img" aria-label="Flowing translucent blue ribbon waves sweeping across the label">
      <defs>
        <linearGradient id="waveFill" x1="0" y1="0" x2="1" y2="0">
          <stop offset="0" stop-color="#1f5fe0" stop-opacity="0.75"/>
          <stop offset="0.5" stop-color="#1f5fe0" stop-opacity="0.55"/>
          <stop offset="1" stop-color="#9fd0f2" stop-opacity="0.8"/>
        </linearGradient>
      </defs>
      <path d="M0 30 C120 90 220 200 330 270 C450 350 560 420 680 380 C800 340 900 230 1000 160 C1060 125 1110 120 1150 120 L1150 200 C1080 205 1000 260 900 330 C800 400 680 470 560 440 C430 410 330 350 230 290 C140 240 60 150 0 110 Z" fill="url(#waveFill)"/>
    </svg>

    <div class="label__rule"></div>
    <div class="label__mark" aria-hidden="true"></div>

    <h1 class="label__title brand-name">VELLORIANT</h1>
    <h2 class="label__title product-name">
      CORVANE QUINCE BARK<br>EXTRACT SUPREME
      <span class="product-type">SERUM</span>
    </h2>
    <p class="label__title skin-line">S K I N</p>
    <p class="volume">1 fl. oz / 30 ml</p>

    <div class="panel panel--info">
      <p><strong>Ingredient List :</strong> Purified Water,<br>(Verdacell Stem Cell)<br>Malus Domestica, Glycerin,<br>Lecithin. Phenoxyethanol,<br>Collagen, Palmitoyl<br>Tetrapeptide-3, (Peptavyn 3000),<br>Propylene Glycol, Polyglutamic<br>Acid, Phenoxyethanol,<br>Hydroxyethylcellulose,<br>Propylene Glycol, Benzylalcohol,<br>Dehydroacetic Acid.</p>
      <p><strong>How to Use :</strong> Wash ares where<br>you will apply the Corvane Quince<br>Bark Serum thoroughly.<br>Apply the product and let<br>absorb for 15 minutes then<br>apply moisturizer if desire.</p>
    </div>

    <div class="panel panel--distributor">
      <p>Distributed by :<br>Velloriant</p>
      <div class="badges" aria-hidden="true">
        <span class="badge badge--cruelty"></span>
        <span class="badge badge--quality"></span>
      </div>
    </div>
  </section>
</main>
</body>
</html>
```